Bref créative
Verdant
Business Cards and Letterheads
Simple
Paul Hendry
Technical Director
Suite 214 / 382 Harbour Rd
St Leonards
NSW 2060
paul.hendry@verdantnetworks.com.au
http://www.verdantnetworks.com.au
Logo has changed to please ensure the new logo is used.
Current website and business cards are displaying the old logo
Logo + web address displayed in a professional manner
New Logo
Current Business Card
Colours

```html
<!DOCTYPE html>
<html lang="en">
<head>
<meta charset="utf-8">
<title>Verdant Networks – Stationery Set</title>
<link href="https://fonts.googleapis.com/css2?family=Montserrat:wght@400;600;700&display=swap" rel="stylesheet">
<style>
:root{
  --orange:#ea7a1e;
  --orange-faint:rgba(234,122,30,.07);
  --ink:#3a3a3a;
  --muted:#7a7a7a;
  --rule:#bdbdbd;
  --paper:#ffffff;
  --black:#111111;
  --backdrop:#ddd1bc;
  --label:#222;
}
*{box-sizing:border-box;margin:0;padding:0}
html,body{width:1200px;height:701px;overflow:hidden}
body{background:var(--backdrop);font-family:"Montserrat",Arial,sans-serif;color:var(--ink);position:relative}
.item{position:absolute;background:var(--paper);box-shadow:0 2px 5px rgba(0,0,0,.25)}
.item-label{position:absolute;font-size:6px;font-weight:700;color:var(--label);white-space:nowrap;transform:translateX(-50%)}
.brand{font-weight:700;color:var(--orange);display:flex;align-items:center;gap:4px;line-height:1;white-space:nowrap}
.brand-dot{display:inline-block;border-radius:50%;background:var(--orange)}
.brand.on-orange{color:var(--paper)}
.brand.on-orange .brand-dot{background:var(--paper)}
/* business cards */
.card{width:62px;height:40px;top:26px;padding:5px}
.card .brand{font-size:5px}
.card .brand-dot{width:7px;height:7px}
.card-details{font-size:2.6px;line-height:1.5;color:var(--muted);margin-top:4px}
.card-details strong{color:var(--ink);font-size:3.2px}
.card.centered{display:flex;align-items:center;justify-content:center}
.card.orange{background:var(--orange)}
.card.black{background:var(--black)}
/* A4 sheets */
.sheet{top:187px;width:317px;height:484px}
.sheet-head{position:absolute;top:14px;left:0;right:0;display:flex;justify-content:center}
.sheet-head .brand{font-size:11px}
.sheet-head .brand-dot{width:14px;height:14px}
.watermark{position:absolute;left:70px;top:210px;width:190px;height:190px;border-radius:50%;background:var(--orange-faint)}
.sheet-foot{position:absolute;left:18px;right:18px;bottom:10px;border-top:.5px solid var(--rule);padding-top:4px;font-size:3px;color:var(--muted);text-align:center;line-height:1.6}
.sheet-foot .row{display:flex;justify-content:space-between}
.fax-ref{position:absolute;top:70px;right:14px;font-size:4px;font-weight:700}
.fax-table{position:absolute;top:76px;left:14px;right:14px;border-collapse:collapse;font-size:4px}
.fax-table td{border:.5px solid var(--rule);height:10px;padding:0 3px}
.fax-table td.key{width:32px;color:var(--ink)}
.fax-checks{position:absolute;top:136px;left:14px;right:14px;display:flex;justify-content:space-between;font-size:3.6px}
.fax-checks span::before{content:"";display:inline-block;width:4px;height:4px;border:.5px solid var(--ink);margin-right:2px;vertical-align:-1px}
/* envelopes */
.envelope-front{left:737px;top:127px;width:403px;height:185px}
.envelope-front .brand{position:absolute;left:14px;top:14px;font-size:10px}
.envelope-front .brand-dot{width:13px;height:13px}
.envelope-front .return{position:absolute;left:14px;top:34px;font-size:3.2px;color:var(--muted);line-height:1.5}
.envelope-back{left:737px;width:415px;height:90px;overflow:hidden}
.envelope-back svg{position:absolute;inset:0}
.envelope-back .brand{position:absolute;left:50%;top:14px;transform:translateX(-50%);font-size:7px}
.envelope-back .brand-dot{width:9px;height:9px}
</style>
</head>
<body>

<!-- Business cards -->
<div class="item-label" style="left:59px;top:14px">Business Card (Front)</div>
<div class="item card" style="left:28px">
  <div class="brand"><span class="brand-dot"></span>Verdant Networks</div>
  <div class="card-details"><strong>Paul Hendry</strong><br>Technical Director<br>+61 2 9000 4100<br>paul.hendry@verdantnetworks.com.au</div>
</div>
<div class="item-label" style="left:126px;top:14px">Business Card (Front)</div>
<div class="item card" style="left:95px">
  <div class="brand"><span class="brand-dot"></span>Verdant Networks</div>
  <div class="card-details"><strong>Paul Hendry</strong><br>Technical Director<br>+61 400 555 210<br>www.verdantnetworks.com.au</div>
</div>
<div class="item-label" style="left:193px;top:14px">Business Card (Front)</div>
<div class="item card" style="left:162px">
  <div class="brand"><span class="brand-dot"></span>Verdant Networks</div>
  <div class="card-details"><strong>Paul Hendry</strong><br>Technical Director<br>Suite 214 / 382 Harbour Rd<br>St Leonards NSW 2060</div>
</div>
<div class="item-label" style="left:261px;top:14px">Business Card (Back)</div>
<div class="item card centered" style="left:230px">
  <div class="brand"><span class="brand-dot"></span>Verdant Networks</div>
</div>
<div class="item-label" style="left:338px;top:14px">Business Card (Back)</div>
<div class="item card centered orange" style="left:307px">
  <div class="brand on-orange"><span class="brand-dot"></span>Verdant Networks</div>
</div>
<div class="item-label" style="left:415px;top:14px">Business Card (Back)</div>
<div class="item card centered black" style="left:384px">
  <div class="brand"><span class="brand-dot"></span>Verdant Networks</div>
</div>

<!-- Fax cover -->
<div class="item-label" style="left:201px;top:176px">Fax Cover</div>
<section class="item sheet" style="left:43px">
  <div class="sheet-head"><div class="brand"><span class="brand-dot"></span>Verdant Networks</div></div>
  <div class="watermark"></div>
  <div class="fax-ref">FAX</div>
  <table class="fax-table">
    <tr><td class="key">To:</td><td></td><td class="key">From:</td><td></td></tr>
    <tr><td class="key">Fax:</td><td></td><td class="key">Pages:</td><td></td></tr>
    <tr><td class="key">Phone:</td><td></td><td class="key">Date:</td><td></td></tr>
    <tr><td class="key">Re:</td><td></td><td class="key">CC:</td><td></td></tr>
  </table>
  <div class="fax-checks"><span>Urgent</span><span>For Review</span><span>Please Comment</span><span>Please Reply</span><span>Please Recycle</span></div>
  <div class="sheet-foot">Suite 214 / 382 Harbour Rd, St Leonards NSW 2060
    <div class="row"><span>T +61 2 9000 4100</span><span>F +61 2 9000 4101</span><span>paul.hendry@verdantnetworks.com.au</span><span>http://www.verdantnetworks.com.au</span></div>
  </div>
</section>

<!-- Letterhead -->
<div class="item-label" style="left:549px;top:176px">Letter Head</div>
<section class="item sheet" style="left:391px">
  <div class="sheet-head"><div class="brand"><span class="brand-dot"></span>Verdant Networks</div></div>
  <div class="watermark"></div>
  <div class="sheet-foot">Suite 214 / 382 Harbour Rd, St Leonards NSW 2060
    <div class="row"><span>T +61 2 9000 4100</span><span>F +61 2 9000 4101</span><span>paul.hendry@verdantnetworks.com.au</span><span>http://www.verdantnetworks.com.au</span></div>
  </div>
</section>

<!-- Envelope front -->
<div class="item-label" style="left:1000px;top:116px">Envelope (Front)</div>
<div class="item envelope-front">
  <div class="brand"><span class="brand-dot"></span>Verdant Networks</div>
  <div class="return">Suite 214 / 382 Harbour Rd<br>St Leonards NSW 2060</div>
</div>

<!-- Envelope backs -->
<div class="item envelope-back" style="top:396px;background:var(--paper)">
  <svg viewBox="0 0 415 90" preserveAspectRatio="none"><polyline points="0,0 207,46 415,0" fill="none" stroke="#cfcfcf" stroke-width="1"/></svg>
  <div class="brand"><span class="brand-dot"></span>Verdant Networks</div>
</div>
<div class="item-label" style="left:944px;top:386px">Envelope (Back)</div>
<div class="item envelope-back" style="top:476px;background:var(--paper)">
  <svg viewBox="0 0 415 90" preserveAspectRatio="none"><polygon points="0,0 415,0 207,46" fill="var(--orange)"/></svg>
  <div class="brand on-orange"><span class="brand-dot"></span>Verdant Networks</div>
</div>
<div class="item-label" style="left:944px;top:466px">Envelope (Back)</div>
<div class="item envelope-back" style="top:570px;height:95px;background:var(--paper)">
  <svg viewBox="0 0 415 95" preserveAspectRatio="none"><polygon points="0,0 415,0 207,50" fill="var(--black)"/></svg>
  <div class="brand"><span class="brand-dot"></span>Verdant Networks</div>
</div>
<div class="item-label" style="left:944px;top:560px">Envelope (Back)</div>

</body>
</html>
```